Varlow Industries Luxury Candles

Luxury box design,, simple and sophisticated look,,

My collection of candles come in 5 different fragrances, i would like to be able to change the fragrance name on the boxes,,,,

I would like the outline of australia on the front down the bottom , (only small) to represent this is an australian product.

My boxes are white gloss,,,

Happy for you to use my current logo ,,, however you'll have to change Varlow Nails to Varlow Industries.

```html
<!DOCTYPE html>
<html lang="en">
<head>
<meta charset="UTF-8">
<title>Varlow Industries – Vanilla Caramel Candle Box</title>
<link rel="stylesheet" href="https://fonts.googleapis.com/css2?family=Zilla+Slab:wght@300;400&display=swap">
<style>
  :root {
    --paper: #ffffff;
    --backdrop: #ffffff;
    --gold: #c9a42c;
    --gold-line: #d1ae3a;
    --ink: #2f2f2f;
    --marble-grey: #d9d9d9;
    --marble-dark: #4a4a4a;
    --marble-cream: #f4efe6;
  }
  * { box-sizing: border-box; margin: 0; padding: 0; }
  html, body {
    width: 1200px; height: 960px; overflow: hidden;
    background: var(--backdrop);
    font-family: "Zilla Slab", Georgia, serif;
    color: var(--ink);
  }
  .canvas {
    position: relative; width: 1200px; height: 960px;
  }
  .box-panel {
    position: absolute; top: 190px;
    width: 400px; height: 580px;
    background: var(--paper);
    box-shadow: 0 0 0 1px #ececec;
    overflow: hidden;
  }
  .box-panel--back { left: 150px; }
  .box-panel--front { left: 650px; }
  .lid-band {
    position: absolute; top: 0; left: 0; right: 0; height: 34px;
    background: var(--gold);
  }
  .marble-field {
    position: absolute; top: 34px; left: 0; right: 0; bottom: 0;
    background:
      radial-gradient(ellipse 30% 60% at 20% 30%, rgba(74,74,74,.35), transparent 70%),
      radial-gradient(ellipse 25% 70% at 85% 40%, rgba(74,74,74,.3), transparent 70%),
      radial-gradient(ellipse 50% 40% at 50% 20%, rgba(201,164,44,.22), transparent 70%),
      radial-gradient(ellipse 60% 50% at 40% 80%, rgba(217,217,217,.6), transparent 70%),
      linear-gradient(160deg, var(--paper), var(--marble-cream) 60%, var(--paper));
  }
  .label {
    position: absolute; background: var(--paper);
    border: 2px solid var(--gold-line);
    text-align: center;
  }
  .label--back {
    left: 56px; top: 116px; width: 264px; height: 416px;
    padding: 28px 20px;
  }
  .label--front {
    left: 60px; top: 196px; width: 252px; height: 240px;
    padding: 34px 14px 0;
  }
  .fragrance-name {
    color: var(--gold); font-weight: 400; text-transform: uppercase;
    letter-spacing: .02em;
  }
  .label--back .fragrance-name { font-size: 18px; margin-bottom: 20px; }
  .label--front .fragrance-name { font-size: 23px; margin-top: 34px; }
  .description {
    font-size: 12.5px; line-height: 1.45; font-weight: 400; margin-bottom: 16px;
  }
  .producer {
    position: absolute; left: 0; right: 0; bottom: 26px;
    font-size: 11.5px; line-height: 1.4;
  }
  .brand-name {
    font-size: 24px; font-weight: 300; color: var(--ink);
  }
  .net-weight { font-size: 11px; margin-top: 22px; }
  .product-note { font-size: 9px; line-height: 1.35; margin-top: 6px; }
  .origin-mark {
    position: absolute; left: 14px; bottom: 26px;
    width: 62px; height: 52px; border-radius: 18px 22px 14px 20px;
    background: var(--gold);
  }
</style>
</head>
<body>
<main class="canvas">
  <section class="box-panel box-panel--back">
    <div class="lid-band"></div>
    <div class="marble-field" role="img" aria-label="White marble pattern with grey, black and gold veins"></div>
    <div class="label label--back">
      <h2 class="fragrance-name">Vanilla Caramel</h2>
      <p class="description">Lorem ipsum dolor sit amet, consectetuer adipiscing elit, sed diam nonummy nibh euismod tincidunt ut laoreet dolore magna aliquam erat volutpat. Ut wisi enim ad</p>
      <p class="description">Lorem ipsum dolor sit amet, consectetuer adipiscing elit, sed diam nonummy nibh euismod tincidunt ut laoreet dolore magna aliquam erat volutpat. Ut wisi enim ad Lorem ipsum dolor sit amet, consec</p>
      <p class="producer">Produced by<br>VARLOW INDUSTRIES<br>MADE IN AUSTRALIA</p>
    </div>
  </section>

  <section class="box-panel box-panel--front">
    <div class="lid-band"></div>
    <div class="marble-field" role="img" aria-label="White marble pattern with grey, black and gold veins"></div>
    <div class="label label--front">
      <h1 class="brand-name">Varlow Industries</h1>
      <h2 class="fragrance-name">Vanilla Caramel</h2>
      <p class="net-weight">11 oz.</p>
      <p class="product-note">hand-poured made with 100% wax<br>natural soy candle made with fine fragrances</p>
    </div>
    <div class="origin-mark" role="img" aria-label="Small gold outline map of Australia"></div>
  </section>
</main>
</body>
</html>
```